Carpet cleaning company wants business card

Need an exciting new fresh design for business cards for my carpet cleaning /pest control business
www.brightwovecare.com.au
Can design include a lined section for quoting or information? Thanks !

```html
<!DOCTYPE html>
<html lang="en">
<head>
<meta charset="utf-8">
<title>Brightwove Care – Business Cards</title>
<link href="https://fonts.googleapis.com/css2?family=Roboto:wght@400;500;700&display=swap" rel="stylesheet">
<style>
  :root {
    --blue: #0d58a6;
    --red: #ed4138;
    --ink: #1d1d1f;
    --white: #ffffff;
    --stage: #2a2a2c;
  }
  * { box-sizing: border-box; margin: 0; padding: 0; }
  html, body { width: 1200px; height: 792px; overflow: hidden; }
  body {
    background: var(--stage);
    font-family: "Roboto", Arial, sans-serif;
    position: relative;
  }
  .card {
    position: absolute;
    width: 497px;
    height: 276px;
    background: var(--white);
    border-radius: 20px;
    overflow: hidden;
  }
  .card--a { left: 96px;  top: 100px; }
  .card--b { left: 607px; top: 100px; }
  .card--c { left: 96px;  top: 401px; height: 292px; }
  .card--d { left: 607px; top: 401px; height: 292px; }

  .brand {
    position: absolute;
    top: 26px; left: 0; right: 0;
    display: flex; justify-content: center; align-items: center; gap: 10px;
  }
  .brand__mark { width: 18px; height: 18px; background: var(--red); }
  .brand__name {
    font-weight: 700; font-size: 38px; color: var(--blue);
    letter-spacing: -0.5px; line-height: 1;
  }

  .services {
    position: absolute; top: 98px; left: 0; right: 0;
    text-align: center; font-size: 14px; color: var(--ink); line-height: 19px;
  }
  .card--c .services, .card--d .services { top: 104px; }
  .services span::before {
    content: "•"; color: var(--red); margin: 0 3px 0 6px;
  }

  .band {
    position: absolute; left: 0; right: 0; top: 150px; height: 77px;
    display: flex;
  }
  .card--c .band, .card--d .band { top: 159px; height: 82px; }
  .band__person {
    width: 239px; background: var(--blue); color: var(--white);
    text-align: right; padding-right: 16px;
    display: flex; flex-direction: column; justify-content: center;
  }
  .person__name { font-weight: 700; font-size: 21px; line-height: 24px; }
  .person__role { font-size: 14.5px; line-height: 20px; }
  .band__contact {
    flex: 1; background: var(--red); color: var(--white);
    padding-left: 12px;
    display: flex; flex-direction: column; justify-content: center; gap: 2px;
    font-size: 14px; line-height: 17px;
  }
  .contact__line { display: flex; align-items: center; gap: 5px; }
  .contact__line svg { width: 12px; height: 12px; flex: none; }

  .address {
    position: absolute; left: 0; right: 0; bottom: 18px;
    display: flex; justify-content: center; align-items: center; gap: 6px;
    font-size: 14.5px; color: var(--ink);
  }
  .card--c .address, .card--d .address { bottom: 26px; }
  .address svg { width: 11px; height: 15px; }
</style>
</head>
<body>

<svg width="0" height="0" style="position:absolute">
  <defs>
    <symbol id="icon-phone" viewBox="0 0 24 24"><path fill="#fff" d="M2 8c0-3 5-5 10-5s10 2 10 5v2h-5V8c-1-1-3-1.5-5-1.5S8 7 7 8v2H2zM5 12h14l2 8H3z"/></symbol>
    <symbol id="icon-mail" viewBox="0 0 24 24"><path fill="#fff" d="M1 4h22v16H1zM3 6v1l9 6 9-6V6l-9 6z"/></symbol>
    <symbol id="icon-web" viewBox="0 0 24 24"><circle cx="12" cy="12" r="10" fill="#fff"/><path fill="#ed4138" d="M8 6c2 0 3 2 2 4s-3 1-3 3-2 1-3 0c0-3 2-7 4-7zm7 6c2 0 3 2 2 4s-2 3-3 2-1-3-1-4 1-2 2-2z"/></symbol>
    <symbol id="icon-pin" viewBox="0 0 22 30"><path fill="#ed4138" d="M11 0C5 0 0 5 0 11c0 8 11 19 11 19s11-11 11-19C22 5 17 0 11 0zm0 15a4 4 0 1 1 0-8 4 4 0 0 1 0 8z"/></symbol>
  </defs>
</svg>

<article class="card card--a">
  <div class="brand"><span class="brand__mark"></span><span class="brand__name">Brightwove Care</span></div>
  <p class="services"><span>Carpet Cleaning</span><span>Tile &amp; Grout Cleaning</span><span>Upholstery Cleaning</span><br><span>Pest Control Services</span></p>
  <div class="band">
    <div class="band__person"><div class="person__name">DANIEL HARTLEY</div><div class="person__role">Technician</div></div>
    <div class="band__contact">
      <div class="contact__line"><svg><use href="#icon-phone"/></svg>07 4100 2288</div>
      <div class="contact__line"><svg><use href="#icon-mail"/></svg>admin@brightwovecare.com.au</div>
      <div class="contact__line"><svg><use href="#icon-web"/></svg>www.brightwovecare.com.au</div>
    </div>
  </div>
  <div class="address"><svg><use href="#icon-pin"/></svg>PO BOX 318 Cairns QLD 4870</div>
</article>

<article class="card card--b">
  <div class="brand"><span class="brand__mark"></span><span class="brand__name">Brightwove Care</span></div>
  <p class="services"><span>Carpet Cleaning</span><span>Tile &amp; Grout Cleaning</span><span>Upholstery Cleaning</span><br><span>Pest Control Services</span></p>
  <div class="band">
    <div class="band__person"><div class="person__name">OWEN BLAKELY</div><div class="person__role">Technician</div></div>
    <div class="band__contact">
      <div class="contact__line"><svg><use href="#icon-phone"/></svg>07 4100 2288</div>
      <div class="contact__line"><svg><use href="#icon-mail"/></svg>admin@brightwovecare.com.au</div>
      <div class="contact__line"><svg><use href="#icon-web"/></svg>www.brightwovecare.com.au</div>
    </div>
  </div>
  <div class="address"><svg><use href="#icon-pin"/></svg>PO BOX 318 Cairns QLD 4870</div>
</article>

<article class="card card--c">
  <div class="brand"><span class="brand__mark"></span><span class="brand__name">Brightwove Care</span></div>
  <p class="services"><span>Carpet Cleaning</span><span>Tile &amp; Grout Cleaning</span><span>Upholstery Cleaning</span><br><span>Pest Control Services</span></p>
  <div class="band">
    <div class="band__person"><div class="person__name">RENEE HARTLEY</div><div class="person__role">Technician</div></div>
    <div class="band__contact">
      <div class="contact__line"><svg><use href="#icon-phone"/></svg>07 4100 2288</div>
      <div class="contact__line"><svg><use href="#icon-mail"/></svg>admin@brightwovecare.com.au</div>
      <div class="contact__line"><svg><use href="#icon-web"/></svg>www.brightwovecare.com.au</div>
    </div>
  </div>
  <div class="address"><svg><use href="#icon-pin"/></svg>PO BOX 318 Cairns QLD 4870</div>
</article>

<article class="card card--d">
  <div class="brand"><span class="brand__mark"></span><span class="brand__name">Brightwove Care</span></div>
  <p class="services"><span>Carpet Cleaning</span><span>Tile &amp; Grout Cleaning</span><span>Upholstery Cleaning</span><br><span>Pest Control Services</span></p>
  <div class="band">
    <div class="band__person"><div class="person__name">LIAM PRESCOTT</div><div class="person__role">Technician</div></div>
    <div class="band__contact">
      <div class="contact__line"><svg><use href="#icon-phone"/></svg>07 4100 2288</div>
      <div class="contact__line"><svg><use href="#icon-mail"/></svg>admin@brightwovecare.com.au</div>
      <div class="contact__line"><svg><use href="#icon-web"/></svg>www.brightwovecare.com.au</div>
    </div>
  </div>
  <div class="address"><svg><use href="#icon-pin"/></svg>PO BOX 318 Cairns QLD 4870</div>
</article>

</body>
</html>
```